Harbor Mortgage Relief

Please help us give our website a remake or a FACELIFT. It is not very good but it says what we need it to say. But the design is terrible.
I would like our new design font and logo to be used as the theme.

I also want more photos on the site.

I also want consistency with the pages so they look clean.

We want the professionals to do this, let's see what you got!

Thank you!
Updates

Project Deadline Extended
Reason: I can understand you want to be paid. So I will commit to the fee but I want you to have time to make a KICK ASS website for me dudes! Thanks

HI!  Just wanted to say thanks for your time on these.  A lot are great.  However the firefighters have nothing to do with Foreclosure.  We are saving peoples homes from the bank taking them and selling them.   I LOVE the house photos and the families on the website.  That is the direction we like.  THanks.

THANK U ALL FOR THE WORK!   I like a few ending in the numbers: 147  733  693  536  620  478  727  508     I will go over them and choose one soon.  Thank you.   You will be paid shortly. 

Requirements
Must have
• Bright, Upbeat photos. Color scheme should be in order. We like icons on the bottom. not just text.

```html
<!DOCTYPE html>
<html lang="en">
<head>
<meta charset="utf-8">
<title>Harbor Mortgage Relief</title>
<link href="https://fonts.googleapis.com/css2?family=Arimo:ital,wght@0,400;0,700;1,400&family=Tinos&display=swap" rel="stylesheet">
<style>
  :root {
    --red: #a0161c;
    --red-band: #981519;
    --ink: #111111;
    --text: #333333;
    --navy: #373a4d;
    --rule: #d6d6d6;
    --footer: #e8e8e8;
    --white: #ffffff;
  }
  * { margin: 0; padding: 0; box-sizing: border-box; }
  html, body { width: 1200px; height: 1014px; overflow: hidden; }
  body { position: relative; background: var(--white); font-family: "Arimo", Arial, sans-serif; color: var(--text); }

  .site-header { position: absolute; left: 0; top: 0; width: 1200px; height: 84px; background: var(--white); }
  .brand { position: absolute; display: flex; align-items: center; gap: 8px; }
  .brand-mark { border-radius: 50%; background: var(--red); flex: none; }
  .brand-name { font-weight: 700; color: var(--ink); text-transform: uppercase; line-height: 1.05; }
  .site-header .brand { left: 175px; top: 12px; }
  .site-header .brand-mark { width: 58px; height: 58px; }
  .site-header .brand-name { font-size: 17px; width: 150px; }

  .main-nav { position: absolute; left: 500px; top: 28px; width: 543px; height: 34px; display: flex; border-radius: 4px; overflow: hidden; background: linear-gradient(#3a3a3a, #000); }
  .main-nav a { color: var(--white); text-decoration: none; font-size: 14px; line-height: 34px; text-align: center; border-right: 1px solid #3f3f3f; }
  .main-nav a:last-child { border-right: none; }
  .main-nav a.is-active { background: var(--red); }

  .hero-band { position: absolute; left: 0; top: 84px; width: 1200px; height: 389px; background: var(--red-band); }

  .content-card { position: absolute; left: 157px; top: 120px; width: 886px; height: 787px; background: var(--white); box-shadow: 0 1px 4px rgba(0,0,0,.35); }

  .hero-intro { position: absolute; left: 8px; top: 9px; width: 341px; height: 343px; background: var(--red); color: var(--white); padding: 36px 16px 0 16px; }
  .hero-title { font-size: 25.5px; font-weight: 700; line-height: 38px; letter-spacing: .3px; }
  .hero-title .second { color: var(--ink); display: block; }
  .hero-copy { margin-top: 6px; font-size: 14px; line-height: 19.4px; padding-left: 1px; }
  .btn-more { position: absolute; left: 211px; top: 291px; width: 109px; height: 36px; background: var(--ink); color: var(--white); border-radius: 4px; font-size: 15px; line-height: 36px; text-align: center; text-decoration: none; }

  .hero-photo { position: absolute; left: 357px; top: 9px; width: 520px; height: 343px; background: linear-gradient(100deg, #dfe8ee 0%, #b9c9d4 35%, #6f7f92 60%, #2c3550 80%, #cfdde6 100%); }

  .services { position: absolute; left: 25px; top: 392px; width: 286px; }
  .services h2 { font-size: 28px; font-weight: 700; color: var(--ink); margin-bottom: 8px; }
  .service-list { list-style: none; }
  .service-list li { display: flex; align-items: center; gap: 7px; width: 256px; height: 43px; font-size: 13px; border-bottom: 1px solid var(--rule); }
  .service-list li:first-child { height: 28px; align-items: flex-start; }
  .service-list li:last-child { height: 42px; }
  .service-list svg { flex: none; }

  .experience-badge { position: absolute; left: 25px; top: 700px; width: 286px; height: 58px; background: var(--red); color: var(--white); font-family: "Tinos", "Times New Roman", serif; display: flex; align-items: center; padding-left: 18px; gap: 14px; }
  .experience-badge .years { font-size: 37px; }
  .experience-badge .label { font-size: 16.5px; line-height: 23px; letter-spacing: -.3px; }

  .about { position: absolute; left: 361px; top: 392px; width: 505px; font-size: 12.5px; line-height: 19.4px; }
  .about p + p { margin-top: 19.4px; }

  .testimonial { position: absolute; left: 361px; top: 697px; width: 503px; height: 61px; background: var(--navy); color: var(--white); font-style: italic; font-size: 14.3px; line-height: 19.5px; padding: 11px 16px; }

  .site-footer { position: absolute; left: 0; top: 942px; width: 1200px; height: 72px; background: var(--footer); }
  .site-footer .brand { left: 160px; top: 15px; }
  .site-footer .brand-mark { width: 44px; height: 44px; }
  .site-footer .brand-name { font-size: 12.5px; width: 112px; }
  .footer-info { position: absolute; right: 157px; top: 27px; text-align: right; color: var(--ink); }
  .footer-address { font-size: 12.8px; }
  .footer-copy { font-size: 11.3px; margin-top: 8px; }
</style>
</head>
<body>
  <header class="site-header">
    <div class="brand">
      <span class="brand-mark"></span>
      <span class="brand-name">Harbor Mortgage Relief</span>
    </div>
    <nav class="main-nav">
      <a href="#" class="is-active" style="width:88px">Home</a>
      <a href="#" style="width:94px">About Us</a>
      <a href="#" style="width:94px">Services</a>
      <a href="#" style="width:107px">Contact Us</a>
      <a href="#" style="width:160px">Financing Options</a>
    </nav>
  </header>

  <div class="hero-band"></div>

  <main class="content-card">
    <section class="hero-intro">
      <h1 class="hero-title">HARBOR MORTGAGE <span class="second">RELIEF</span></h1>
      <p class="hero-copy">Specializes in assisting homeowners who are in FORECLOSURE, by offering solid alternatives to losing your home in a Trustee Sale. Having your home foreclosed on can damage your credit for up to 7 years. Most foreclosures end with the home owner being evicted from their home, leaving them with no money, no place to live and without ample time to safely remove their possessions from their home.</p>
      <a href="#" class="btn-more">Learn More</a>
    </section>
    <div class="hero-photo" role="img" aria-label="Photo of a smiling team of business professionals in a bright office"></div>

    <section class="services">
      <h2>What we do</h2>
      <ul class="service-list">
        <li><svg width="14" height="14" viewBox="0 0 14 14"><circle cx="7" cy="7" r="7" fill="#a0161c"/><path d="M3.5 7h5M6.5 4.2 9.5 7l-3 2.8" stroke="#fff" stroke-width="1.8" fill="none"/></svg>Lorem ipsum dolor sit amet</li>
        <li><svg width="14" height="14" viewBox="0 0 14 14"><circle cx="7" cy="7" r="7" fill="#a0161c"/><path d="M3.5 7h5M6.5 4.2 9.5 7l-3 2.8" stroke="#fff" stroke-width="1.8" fill="none"/></svg>Consectetur adipisicing elit</li>
        <li><svg width="14" height="14" viewBox="0 0 14 14"><circle cx="7" cy="7" r="7" fill="#a0161c"/><path d="M3.5 7h5M6.5 4.2 9.5 7l-3 2.8" stroke="#fff" stroke-width="1.8" fill="none"/></svg>Sed ut perspiciatis unde omnis</li>
        <li><svg width="14" height="14" viewBox="0 0 14 14"><circle cx="7" cy="7" r="7" fill="#a0161c"/><path d="M3.5 7h5M6.5 4.2 9.5 7l-3 2.8" stroke="#fff" stroke-width="1.8" fill="none"/></svg>At vero eos et accusamus</li>
        <li><svg width="14" height="14" viewBox="0 0 14 14"><circle cx="7" cy="7" r="7" fill="#a0161c"/><path d="M3.5 7h5M6.5 4.2 9.5 7l-3 2.8" stroke="#fff" stroke-width="1.8" fill="none"/></svg>Lorem ipsum dolor sit amet</li>
        <li><svg width="14" height="14" viewBox="0 0 14 14"><circle cx="7" cy="7" r="7" fill="#a0161c"/><path d="M3.5 7h5M6.5 4.2 9.5 7l-3 2.8" stroke="#fff" stroke-width="1.8" fill="none"/></svg>Denouncing pleasure and praising pain</li>
      </ul>
    </section>

    <div class="experience-badge">
      <span class="years">50</span>
      <span class="label">years of real estate knowledge and experience</span>
    </div>

    <section class="about">
      <p>HARBOR MORTGAGE RELIEF specializes in assisting home owners who are in the foreclosure process. We understand that there are many reasons why homeowners are unable to pay their mortgages and that every situation is in fact unique.</p>
      <p>HARBOR MORTGAGE RELIEF takes the time to meet with homeowners and explain the options you have to the foreclosure process. We have found that in most cases the foreclosure can be prevented. Our specialist will meet with you personally to help assess the situation and offer you other options to foreclosure.</p>
      <p>We have the ability, knowledge and capitol necessary to take decisive action to help stop your home from being foreclosed.</p>
      <p>We are located in Downtown Bayport, CA across the street from the court house. HARBOR MORTGAGE RELIEF covers the entire Southern California Area, from Ventura to the Mexican boarder.</p>
    </section>

    <blockquote class="testimonial">Our skill and integrity has earned us a reputation for the "#1 provider of foreclosure solutions in all of Southern California"</blockquote>
  </main>

  <footer class="site-footer">
    <div class="brand">
      <span class="brand-mark"></span>
      <span class="brand-name">Harbor Mortgage Relief</span>
    </div>
    <div class="footer-info">
      <p class="footer-address">118 Harbor Street, Suite 210 &nbsp;|&nbsp; Bayport, CA 90210 &nbsp;|&nbsp; Ph: 555-014-2290</p>
      <p class="footer-copy">Content copyright 2012. HARBORMORTGAGERELIEF.COM. All rights reserved.</p>
    </div>
  </footer>
</body>
</html>
```